Education Website Re-Design for Non-Profit

We are looking for a re-design of our education website, the RLV Learning center. The Education Center is intended to be the "go to" resource for interactive classrooms and resources on chronic kidney disease and dialysis for patients, family members and interested parties. We are looking for a re-design on the home page and then design the basic pages that host the content on the site. Also, the classroom pages could use a revamp with a Left-Right Menus (nav on left vs. right)

Current website: www.rlvlearnhub.org
Example Basic Page: http://rlvlearnhub.org/diabetes-awareness-month
Classroom Page: http://rlvlearnhub.org/classroom/home-hemodialysis
Updates

Project Deadline Extended
Reason: Need more time to decide on current submissions.

Target Market(s)

Current patients, family members, healthcare professionals

Industry/Entity Type

Education

Coding

Coded - Design and coding required

Number of Pages Required

3 page

Font styles to use
Sans Serif

Colors
0355a3
3176b5
ec1f27
ffffff

Requirements
Must have
• The website is hosted using Drupal 7 and will likely be upgraded to Drupal 8 so as much compatibility with Drupal as possible would be nice. Also we would like it to be a responsive design with two breakpoints for phone/tablet and then tablet/desktop views. Please keep the branding colors and fonts the same as found in the attached draft style guide.
• I'm attaching a screen shot of the Northwind Glucose Society website. We like the layout and cleanliness of the information presented on their homepage and then their subsequent education pages. (url:http://www.glucosefolk.org/?loc=bb)
Nice to have
• I would like to see a clean, semi-modern design. I currently HATE the narrow fixed width design we have with the puzzle piece navigation objects
• Education Topics: Nutrition, Pediatric Kidney Disease, Diabetes, Bone and Mineral Disease, Treatment Options, Heart Disease, Mental Health, Chronic Kidney Disease, CKD Prevention, Emergency Preparedness, Anemia Management and Paying for Dialysis (Like bottom of Northwind Glucose Society)
Should not have
• Narrow fixed width design, white background around text makes it look disjointed and dated, no "educational tools" menu/subpage focus, shouldn't prioritize "advocacy" portion, it should be included but at the bottom. Education topics and tools need to be prioritized.

```html
<!DOCTYPE html>
<html lang="en">
<head>
<meta charset="utf-8">
<title>RLV Learning Center</title>
<link rel="stylesheet" href="https://fonts.googleapis.com/css2?family=Titillium+Web:wght@400;600;700&display=swap">
<style>
:root{
  --brand-blue:#0355a3;
  --mid-blue:#3176b5;
  --brand-red:#ec1f27;
  --white:#ffffff;
  --text:#555a60;
  --light-gray:#f2f2f2;
  --news-gray:#e4e4e4;
  --nav-gray:#e9eaec;
  --footer-black:#0b0b0b;
  --pink:#e8195b;
}
*{box-sizing:border-box;margin:0;padding:0}
html,body{width:766px;height:1200px;overflow:hidden}
body{position:relative;font-family:"Titillium Web",Arial,sans-serif;color:var(--text);background:var(--white)}
.abs{position:absolute}
a{color:inherit;text-decoration:none}

.top-rule{left:0;top:0;width:766px;height:4px;background:var(--brand-blue)}
.site-header{left:0;top:4px;width:766px;height:68px;background:var(--white)}
.brand{left:74px;top:14px;display:flex;align-items:center;gap:7px;color:var(--brand-blue);font-weight:700;font-size:14px;line-height:13px}
.brand-mark{width:36px;height:36px;background:var(--brand-blue);border-radius:50%}
.search{left:476px;top:25px;width:142px;height:26px;border:1px solid #d4d4d4;font-size:8px;color:#888;padding:6px 7px}
.search svg{position:absolute;right:12px;top:8px}
.donate{left:629px;top:25px;width:63px;height:25px;background:#d7201f;color:var(--white);border-radius:4px;font-size:8px;text-align:center;line-height:25px}

.main-nav{left:0;top:72px;width:766px;height:36px;background:linear-gradient(#f1f2f3,#e2e3e6);border-top:1px solid #dcdcdc}
.main-nav a{position:absolute;top:12px;font-size:7.5px;font-weight:600;color:#222}
.main-nav a.active{color:var(--brand-red)}

.hero{left:0;top:108px;width:766px;height:336px;background:linear-gradient(120deg,#3a78b2 0%,#2f6aa7 45%,#3b7db7 70%,#2c67a3 100%)}
.hero-main{left:74px;top:137px;width:427px;height:273px;border:3px solid var(--white);background:linear-gradient(135deg,#6f7d7a,#c9a58c 45%,#d9c2ae 70%,#5a5f61)}
.caption{background:rgba(255,255,255,.82);padding:8px 7px}
.caption h3{color:var(--brand-red);font-size:11px;font-weight:600;line-height:13px}
.caption p{font-size:7.3px;line-height:11.5px;color:#333;margin-top:4px}
.arrow{position:absolute;width:13px;height:13px;border-radius:50%;background:var(--white);border:1px solid #999}
.arrow svg{position:absolute;left:3px;top:3px}
.hero-side{width:174px;height:129px;border:3px solid var(--white)}
.side-one{left:518px;top:137px;background:linear-gradient(135deg,#8a6e55,#e2c9b2 50%,#b33a2e)}
.side-two{left:518px;top:281px;background:linear-gradient(135deg,#d8c9a8,#e8dcc7 45%,#7a6b5a)}
.side-caption{left:6px;width:136px;height:28px;background:rgba(255,255,255,.78);color:var(--brand-red);font-size:10.5px;font-weight:600;padding:6px 7px}
.dots{left:363px;top:421px;display:flex;gap:5px}
.dots span{width:9px;height:9px;border-radius:50%;background:var(--white);border:1px solid #bbb}
.dots span.on{background:var(--brand-red)}

.features{left:0;top:444px;width:766px;height:126px;background:var(--light-gray)}
.feature{top:0;height:126px;text-align:center;padding-top:27px}
.feature.mid{background:linear-gradient(90deg,#eaeaea,#f7f7f7 8%,#f7f7f7 92%,#eaeaea)}
.feature h2{color:var(--brand-red);font-size:15.5px;font-weight:600;line-height:18px}
.feature p{font-size:7.3px;line-height:13.5px;color:#555;margin:6px auto 0;width:180px}
.feature a{font-size:7.3px;color:var(--brand-blue);font-weight:600}

.section-title{color:var(--brand-blue);font-weight:600}
.awareness-title{left:72px;top:592px;font-size:19.5px}
.story-img{width:141px;height:158px}
.story-one-img{left:73px;top:634px;background:linear-gradient(135deg,#c98e88,#e3b2a6 40%,#3d5d86)}
.story-two-img{left:388px;top:634px;background:linear-gradient(135deg,#e9d4c8,#c89d8e 50%,#b47a86)}
.story-text{width:156px}
.story-text h3{color:var(--brand-red);font-size:10px;font-weight:600;margin-top:8px}
.story-text p{font-size:7.3px;line-height:11.5px;color:#555;margin-top:1px}
.btn{position:absolute;width:64px;height:26px;border-radius:5px;background:#d7201f;color:var(--white);font-size:7.5px;text-align:center;line-height:26px}

.news{left:0;top:818px;width:766px;height:204px;background:var(--news-gray)}
.news-title{left:72px;top:834px;font-size:15px}
.news-item{top:866px;width:200px}
.news-item h4{color:#d7201f;font-size:8px;font-weight:600;line-height:15.5px;width:140px}
.news-thumb{position:absolute;left:0;top:38px;width:87px;height:83px;border:1px solid #bbb;background:linear-gradient(135deg,#c9c9c9,#efe7e0 55%,#8a8f96)}
.news-body{position:absolute;left:91px;top:39px;width:108px}
.news-body h5{color:var(--mid-blue);font-size:8px;font-weight:400}
.news-body p{font-size:7.3px;line-height:12px;color:#666;margin-top:1px}
.news-more{position:absolute;left:0;top:130px;font-size:7.5px;color:#d7201f}

.site-footer{left:0;top:1022px;width:766px;height:122px;background:var(--brand-blue)}
.foot-col{top:25px;color:var(--white);font-size:8px;font-weight:600;line-height:15.3px}
.signup-title{left:566px;top:25px;color:var(--white);font-size:8px;font-weight:600}
.email{left:566px;top:44px;width:87px;height:20px;background:var(--white);font-size:7px;color:#333;padding:3px 5px}
.send{left:653px;top:44px;width:38px;height:20px;background:var(--pink);color:var(--white);font-size:7.5px;font-weight:600;text-align:center;line-height:20px}
.social{left:566px;top:77px;display:flex;gap:5px}
.social span{width:16px;height:16px;border-radius:2px;background:#7fa8d3}

.bottom-bar{left:0;top:1144px;width:766px;height:56px;background:var(--footer-black);color:var(--white);font-size:8px;text-align:center;line-height:56px}
</style>
</head>
<body>

<div class="abs top-rule"></div>

<header class="abs site-header">
  <div class="abs brand" style="top:10px"><span class="brand-mark"></span><span>RLV<br>LEARNING<br>CENTER</span></div>
  <div class="abs search">Search
    <svg width="8" height="8" viewBox="0 0 8 8"><circle cx="3.2" cy="3.2" r="2.4" fill="none" stroke="#222" stroke-width="1.2"/><line x1="5" y1="5" x2="7.5" y2="7.5" stroke="#222" stroke-width="1.3"/></svg>
  </div>
  <a class="abs donate" href="#">Donate</a>
</header>

<nav class="abs main-nav">
  <a class="active" href="#" style="left:99px">Fundraise</a>
  <a href="#" style="left:172px">Resources</a>
  <a href="#" style="left:247px">Policy Take Action</a>
  <a href="#" style="left:346px">Who We Are</a>
  <a href="#" style="left:427px">Educational Tools</a>
  <a href="#" style="left:524px">RLV Classroom</a>
  <a href="#" style="left:614px">Contact Us</a>
</nav>

<section class="abs hero"></section>
<div class="abs hero-main" role="img" aria-label="Group of students gathered around a laptop in a classroom">
  <div class="abs caption" style="left:241px;top:155px;width:174px;height:106px">
    <h3>Lorem ipsum dolor sit</h3>
    <p>Lorem ipsum dolor sit amet, consectetuer adipiscing elit, sed diam nonummy nibh euismod tincidunt ut laoreet dolore magna aliquam erat volutpat.</p>
    <span class="arrow" style="left:150px;top:80px"><svg width="7" height="7" viewBox="0 0 7 7"><path d="M2 1l3 2.5L2 6" fill="none" stroke="#333" stroke-width="1.3"/></svg></span>
  </div>
</div>
<div class="abs hero-side side-one" role="img" aria-label="Student holding a red book in a library">
  <div class="abs side-caption" style="top:68px">Lorem ipsum dolor sit
    <span class="arrow" style="left:140px;top:7px"><svg width="7" height="7" viewBox="0 0 7 7"><path d="M2 1l3 2.5L2 6" fill="none" stroke="#333" stroke-width="1.3"/></svg></span>
  </div>
</div>
<div class="abs hero-side side-two" role="img" aria-label="Crowd of students walking on campus">
  <div class="abs side-caption" style="top:78px">Lorem ipsum dolor sit
    <span class="arrow" style="left:140px;top:7px"><svg width="7" height="7" viewBox="0 0 7 7"><path d="M2 1l3 2.5L2 6" fill="none" stroke="#333" stroke-width="1.3"/></svg></span>
  </div>
</div>
<div class="abs dots"><span class="on"></span><span></span><span></span></div>

<section class="abs features">
  <div class="abs feature" style="left:59px;width:210px">
    <h2>Advocacy</h2>
    <p>Lorem ipsum dolor sit amet, consectetuer adipiscing elit, sed diam nonummy nibh euismod tincidunt ut laoreet dolore magna aliquam</p>
    <a href="#">Read more</a>
  </div>
  <div class="abs feature mid" style="left:273px;width:222px">
    <h2>Education</h2>
    <p>Lorem ipsum dolor sit amet, consectetuer adipiscing elit, sed diam nonummy nibh euismod tincidunt ut laoreet dolore magna aliquam</p>
    <a href="#">Read more</a>
  </div>
  <div class="abs feature" style="left:495px;width:210px">
    <h2>JOIN RLV!</h2>
    <p>Lorem ipsum dolor sit amet, consectetuer adipiscing elit, sed diam nonummy nibh euismod tincidunt ut laoreet dolore magna aliquam</p>
    <a href="#">Read more</a>
  </div>
</section>

<h2 class="abs section-title awareness-title">Diabetes Awareness Month</h2>
<div class="abs story-img story-one-img" role="img" aria-label="Fingertip blood sample on a glucose test strip"></div>
<div class="abs story-text" style="left:222px;top:634px">
  <h3>Lorem Ipsum dolar</h3>
  <p>Lorem ipsum dolor sit amet, consectetuer adipiscing elit, sed diam nonummy nibh euismod tincidunt ut laoreet dolore magna aliquam erat volutpat. Ut wisi enim ad minim veniam, quis nostrud exerci tation ullamcorper suscipit lobortis nisl ut aliquip ex ea commodo consequat. Lorem ipsum dolor sit amet, consectetuer</p>
</div>
<a class="btn" href="#" style="left:222px;top:756px">Read more</a>
<div class="abs story-img story-two-img" role="img" aria-label="Insulin pen held close up"></div>
<div class="abs story-text" style="left:541px;top:634px">
  <h3>Lorem Ipsum dolar</h3>
  <p>Lorem ipsum dolor sit amet, consectetuer adipiscing elit, sed diam nonummy nibh euismod tincidunt ut laoreet dolore magna aliquam erat volutpat. Ut wisi enim ad minim veniam, quis nostrud exerci tation ullamcorper suscipit lobortis nisl ut aliquip ex ea commodo consequat. Lorem ipsum dolor sit amet, consectetuer</p>
</div>
<a class="btn" href="#" style="left:541px;top:756px">Read more</a>

<section class="abs news"></section>
<h2 class="abs section-title news-title">RLV News</h2>
<article class="abs news-item" style="left:73px">
  <h4>Honoring My Father on PKD Awareness Day</h4>
  <div class="news-thumb" role="img" aria-label="Student with books in front of a chalkboard"></div>
  <div class="news-body"><h5>Lorem ipsum dolor sit amet</h5><p>Lorem ipsum dolor sit amet, consetetur sadipscing elitr, sed diam nonumy eirmod tempor sadipscing.</p></div>
  <a class="news-more" href="#">Read more &gt;&gt;</a>
</article>
<article class="abs news-item" style="left:282px">
  <h4>Honoring My Father on PKD Awareness Day</h4>
  <div class="news-thumb" role="img" aria-label="Two students studying together"></div>
  <div class="news-body"><h5>Lorem ipsum dolor sit amet</h5><p>Lorem ipsum dolor sit amet, consetetur sadipscing elitr, sed diam nonumy eirmod tempor sadipscing.</p></div>
  <a class="news-more" href="#">Read more &gt;&gt;</a>
</article>
<article class="abs news-item" style="left:495px">
  <h4>Honoring My Father on PKD Awareness Day</h4>
  <div class="news-thumb" role="img" aria-label="Graduate in cap with a stack of books"></div>
  <div class="news-body"><h5>Lorem ipsum dolor sit amet</h5><p>Lorem ipsum dolor sit amet, consetetur sadipscing elitr, sed diam nonumy eirmod tempor sadipscing.</p></div>
  <a class="news-more" href="#">Read more &gt;&gt;</a>
</article>

<footer class="abs site-footer">
  <div class="abs foot-col" style="left:73px">WHO WE ARE<br>About<br>Mission<br>Values</div>
  <div class="abs foot-col" style="left:165px">Our Work<br>Board Members<br>Financials<br>Contact Info<br>Staff</div>
  <div class="abs foot-col" style="left:276px">CHRONIC KIDNEY DISEASE<br>PATIENT &amp; FAMILY RESOURCES<br>DONATE</div>
  <div class="abs foot-col" style="left:442px">EDUCATION<br>ADVOCACY<br>JOIN US<br>CONTACT US</div>
  <div class="abs signup-title">SIGN UP FOR DAILY INSPIRATION</div>
  <div class="abs email">Email ddress</div>
  <div class="abs send">Send</div>
  <div class="abs social"><span></span><span></span><span></span><span></span></div>
</footer>

<div class="abs bottom-bar">Copyright © RLV Learning All rights reserved.</div>

</body>
</html>
```